Exciting business card design for diesel performance and offroad business!!

We need a business card design that looks good and stands out. I don't want a plain old boring business card that you forget about and throw away at the end of the day. We are a diesel performance and truck accessory business that sell and install the industries biggest brands and best parts out there!

Industry/Entity Type

Business

Contact Information for Business Card

Davin Throope (Owner) 260-555-0173
steadfast.garage@mailvoro.com
Truck and Off-Road Performance and Accessories

Requirements
Must have
• A great look and feel about it. My logo needs to be in center of the card just like the attached picture. On the back I want it to have a list of items we offer
• Truck and Vorn: Lift and Leveling Kits, Intake and Exhaust Systems, Custom Tuning, Wheels and Tires, Steps, Bed Covers, Floor Liners, Custom Lighting, Turbos and Piping, Gauges, Much More!
• UTV: Suspension, Roll Cage, Doors, Exhaust, Tuning, Turbo Kits, Stereo, Wheels/Tires, Custom Lighting, Clutching, Much More!!

```html
<!DOCTYPE html>
<html lang="en">
<head>
<meta charset="utf-8">
<title>Steadfast Garage – Business Card</title>
<link href="https://fonts.googleapis.com/css2?family=Orbitron:wght@400;500;700&display=swap" rel="stylesheet">
<style>
  :root{
    --stage:#1b1b1d;
    --card-black:#0b0b0c;
    --silver:#cfd3d8;
    --silver-dark:#6f747a;
    --red:#e2232a;
    --white:#f4f4f4;
  }
  html,body{margin:0;padding:0;overflow:hidden;}
  body{
    width:1200px;height:800px;background:var(--stage);
    font-family:"Orbitron",sans-serif;position:relative;
  }
  .card{
    position:absolute;width:600px;height:343px;left:300px;
    background:var(--card-black);overflow:hidden;
    box-shadow:0 10px 30px rgba(0,0,0,.6);
  }
  .card-back{top:36px;}
  .card-front{top:421px;}

  .card-art{position:absolute;inset:0;}

  .service-group{position:absolute;color:var(--white);}
  .service-group h3{margin:0 0 4px;font-size:13px;font-weight:500;letter-spacing:.5px;}
  .service-list{margin:0;padding:0;list-style:none;}
  .service-list li{font-size:10.5px;line-height:13.5px;display:flex;align-items:center;gap:6px;white-space:nowrap;}
  .service-list li::before{
    content:"";width:7px;height:7px;border-radius:50%;
    background:var(--red);box-shadow:0 0 0 1.5px rgba(226,35,42,.45);flex:none;
  }
  .group-truck{left:26px;top:20px;}
  .group-utv{left:410px;top:132px;}

  .owner{position:absolute;left:26px;top:196px;}
  .owner-name{margin:0;color:var(--white);font-size:19px;font-weight:500;letter-spacing:.5px;}
  .owner-role{margin:2px 0 0;color:var(--red);font-size:12px;font-weight:500;}

  .contact{position:absolute;left:140px;top:238px;text-align:right;width:250px;}
  .contact-phone{margin:0;color:var(--white);font-size:25px;font-weight:700;letter-spacing:1px;}
  .contact-email{margin:3px 0 0;color:#d6d6d6;font-size:9.5px;}

  .tagline{
    position:absolute;left:0;right:0;bottom:0;height:40px;
    background:var(--red);color:var(--white);
    display:flex;align-items:center;padding-left:26px;
    font-size:14px;margin:0;
  }

  .brand{
    position:absolute;inset:0;display:flex;align-items:center;justify-content:center;gap:16px;
  }
  .brand-mark{width:34px;height:34px;border-radius:50%;background:var(--silver);}
  .brand-name{margin:0;color:var(--silver);font-size:30px;font-weight:700;letter-spacing:3px;}
</style>
</head>
<body>

<section class="card card-back" aria-label="Card back">
  <svg class="card-art" width="600" height="343" viewBox="0 0 600 343">
    <defs>
      <linearGradient id="silverBar" x1="0" y1="0" x2="1" y2="0">
        <stop offset="0" stop-color="#6f747a"/>
        <stop offset=".5" stop-color="#cfd3d8"/>
        <stop offset="1" stop-color="#6f747a"/>
      </linearGradient>
      <linearGradient id="carbonFill" x1="0" y1="0" x2="1" y2="1">
        <stop offset="0" stop-color="#222225"/>
        <stop offset="1" stop-color="#0e0e10"/>
      </linearGradient>
    </defs>
    <rect width="600" height="343" fill="var(--card-black)"/>
    <rect role="img" aria-label="Carbon hexagon texture panel" x="0" y="160" width="600" height="143" fill="url(#carbonFill)"/>
    <polygon points="330,84 600,84 600,118 385,118 362,92 330,92" fill="#2a2b2e"/>
    <polyline points="330,84 360,84 386,118 600,118" fill="none" stroke="url(#silverBar)" stroke-width="4"/>
    <polyline points="0,186 270,186 300,228 390,228" fill="none" stroke="url(#silverBar)" stroke-width="3"/>
    <line x1="0" y1="292" x2="390" y2="292" stroke="#6f747a" stroke-width="2"/>
  </svg>

  <div class="service-group group-truck">
    <h3>TRUCK AND VORN</h3>
    <ul class="service-list">
      <li>Lift and leveling kits</li>
      <li>intake and exhaust systems</li>
      <li>custom tuning</li>
      <li>wheels and tires</li>
      <li>steps, bed covers</li>
      <li>floor liners</li>
      <li>custom lighting</li>
      <li>turbos, etc</li>
    </ul>
  </div>

  <div class="service-group group-utv">
    <h3>UTV</h3>
    <ul class="service-list">
      <li>Suspension</li>
      <li>Roll Cage</li>
      <li>doors</li>
      <li>exhaust</li>
      <li>tuning</li>
      <li>turbo kits</li>
      <li>stereo</li>
      <li>wheels/tires</li>
      <li>custom lighting</li>
      <li>clutching, etc.</li>
    </ul>
  </div>

  <div class="owner">
    <p class="owner-name">DAVIN THROOPE</p>
    <p class="owner-role">OWNER</p>
  </div>

  <div class="contact">
    <p class="contact-phone">260-555-0173</p>
    <p class="contact-email">steadfast.garage@mailvoro.com</p>
  </div>

  <p class="tagline">Truck and offroad performance and Accessories</p>
</section>

<section class="card card-front" aria-label="Card front">
  <svg class="card-art" width="600" height="343" viewBox="0 0 600 343">
    <defs>
      <radialGradient id="asphalt" cx=".5" cy=".45" r=".7">
        <stop offset="0" stop-color="#3a3a3c"/>
        <stop offset="1" stop-color="#141415"/>
      </radialGradient>
    </defs>
    <rect role="img" aria-label="Dark asphalt texture background" width="600" height="343" fill="url(#asphalt)"/>
  </svg>
  <div class="brand">
    <span class="brand-mark"></span>
    <p class="brand-name">STEADFAST GARAGE LLC</p>
  </div>
</section>

</body>
</html>
```